Flyer/Poster to promote Bicycle Race

We need a flyer that promotes a bicycle race in downtown Denver. It need to inspire spectators to come watch and bicycle racers to come race. It benefits the Cedar Hollow Cycling Club is getting urban kids on bikes; sharing healthy lifestyle and values
. We want the colors to be the colors of the logo - blue & red. Community Partnerships must have their logos on the flyer. Flyer must be able to be printed in 8 1/2 x 11 and 11 x 17

Target Market(s)

Neighborhood residents, athletes, cyclists

Industry/Entity Type

Non Profit

Font styles to use
Serif
Sans Serif

Colors
0592cd
ec1f27

Requirements
Must have
• Sunday, July 31, 2016
• Schedule:
• • Racing starts at 7:00am
• • Fun Ride on the Race Course at 12pm
• • Expo & Festival 10am – 6pm
• A Bike Race for Amateurs and Professionals
• A Bike Race for the young, the old & everyone in the middle.
• Great for spectators. Hang out, watch the action & explore the Festival
• Grab a bite to eat & cheer on the racers as they fly around the corners
• Special activities for kids: Pelton Course, Barnaby the Goat & More!!
• Teodoro Vasquez WLMR Music Director and Afternoon by the Creekside host will be onsite!
• Start/Finish/Festival will be on Harlow St between 4th Ave & 6th Ave
• Net proceeds benefit the Cedar Hollow Cycling Club dedicated to getting urban youth on bikes; sharing healthy lifestyle and values
• Special thanks to the Pemberton Foundation for their ongoing support
• HARLOWLOOPRACE.COM

```html
<!DOCTYPE html>
<html lang="en">
<head>
<meta charset="utf-8">
<title>Harlow St Loop Race Flyer</title>
<link href="https://fonts.googleapis.com/css2?family=Kalam:wght@400;700&family=Oswald:wght@500;700&display=swap" rel="stylesheet">
<style>
  :root{
    --stage:#d9d9d9;
    --paper:#ffffff;
    --red:#ec1f27;
    --blue:#0592cd;
    --ink:#1b1b1b;
    --yellow:#f5e32a;
    --brown:#8a4a1c;
    --olive:#6f7f1f;
    --olive-dark:#4a4a26;
    --frame:#b8a24a;
  }
  *{box-sizing:border-box;margin:0;padding:0}
  html,body{width:1200px;height:1200px;overflow:hidden}
  body{background:var(--stage);font-family:"Kalam",cursive}
  .flyer{position:absolute;left:160px;top:30px;width:880px;height:1140px;background:var(--ink);overflow:hidden;box-shadow:0 6px 24px rgba(0,0,0,.25)}
  .partners{position:absolute;left:0;top:0;width:880px;height:150px;background:var(--paper);display:flex;flex-wrap:wrap;align-content:center;justify-content:center;gap:10px 22px;padding:14px 30px}
  .partner{display:flex;align-items:center;gap:6px;font-family:"Oswald",sans-serif;font-weight:500;font-size:15px;color:var(--ink)}
  .partner i{display:block;width:14px;height:14px;background:var(--blue)}
  .partner i.round{border-radius:50%;background:var(--red)}
  .race-photo{position:absolute;left:0;top:150px;width:880px;height:730px;background:linear-gradient(160deg,#c9d3c6 0%,#8f8a99 30%,#5b4a6e 55%,#6a6a66 80%,#4a4a48 100%)}
  .banner{position:absolute;left:150px;top:175px;width:700px;height:128px;background:#f4f4f4;padding:8px 14px;text-align:center;font-family:"Oswald",sans-serif;border:3px solid #ddd;white-space:nowrap}
  .banner .presents{font-size:20px;color:#333;letter-spacing:1px;text-transform:uppercase;line-height:1.2}
  .banner .title{font-size:33px;font-weight:700;color:var(--red);line-height:1.25}
  .banner .date{font-size:22px;font-weight:700;color:var(--blue);line-height:1.2;text-transform:uppercase;letter-spacing:1px}
  .event-mark{position:absolute;left:40px;top:250px;width:100px;height:100px;background:var(--paper);display:flex;flex-direction:column;align-items:center;justify-content:center;gap:4px;font-family:"Kalam",cursive;font-weight:700;font-size:15px;color:var(--ink);text-align:center;line-height:1.05;padding:6px}
  .event-mark i{width:10px;height:10px;background:var(--red);flex:none}
  .location{position:absolute;left:420px;top:430px;width:260px;height:230px}
  .location svg{position:absolute;inset:0}
  .location p{position:relative;color:#fff;font-size:21px;font-weight:700;line-height:1.15;text-align:center;padding-top:52px}
  .schedule{position:absolute;top:690px;width:240px;height:130px;border-radius:8px;text-align:center;padding-top:14px;box-shadow:0 4px 0 rgba(0,0,0,.35)}
  .schedule .label{color:var(--yellow);font-size:22px;font-weight:700;line-height:1.05}
  .schedule .time{color:#fff;font-size:40px;font-weight:700;line-height:1.15;white-space:nowrap}
  .s-racing{left:40px;background:var(--brown)}
  .s-ride{left:320px;background:var(--olive);top:675px}
  .s-expo{left:600px;background:var(--olive-dark);top:660px}
  .s-expo .time{font-size:36px}
  .details{position:absolute;left:36px;top:835px;width:808px;height:215px;background:var(--red);border:2px solid var(--frame);border-radius:14px;padding:12px 22px;color:#fff}
  .details ul{list-style:none}
  .details li{font-size:16px;line-height:20px;display:flex;gap:8px}
  .details li svg{flex:none;margin-top:4px}
  .details .thanks{margin-top:5px;font-family:"Oswald",sans-serif;font-size:15px;color:var(--yellow);letter-spacing:.5px;text-transform:uppercase}
  .footer{position:absolute;left:0;top:1058px;width:880px;height:82px;background:var(--red);text-align:center;font-family:"Oswald",sans-serif;font-weight:700;line-height:1}
  .footer .more{color:var(--yellow);font-size:22px;padding-top:8px}
  .footer .visit{font-size:40px;color:#fff;margin-top:4px}
  .footer .visit span{color:var(--yellow)}
</style>
</head>
<body>
<main class="flyer">
  <header class="partners">
    <div class="partner"><i></i>Ridgeline Seven</div>
    <div class="partner"><i class="round"></i>Gilt Corner</div>
    <div class="partner"><i class="round"></i>City Patrol</div>
    <div class="partner"><i></i>Cedar Hollow</div>
    <div class="partner"><i></i>Orvex</div>
    <div class="partner"><i class="round"></i>Redspoke</div>
    <div class="partner"><i></i>Sunbolt</div>
    <div class="partner"><i></i>Tallow</div>
    <div class="partner"><i class="round"></i>Peak Public TV</div>
    <div class="partner"><i></i>Velvet Women's Racing</div>
    <div class="partner"><i class="round"></i>WLMR</div>
  </header>

  <div class="race-photo" role="img" aria-label="Pack of road cyclists in helmets racing down a city street toward the camera"></div>

  <div class="banner">
    <div class="presents">Cedar Hollow Cycling Club presents</div>
    <div class="title">Miles Pemberton Memorial Bicycle Race</div>
    <div class="date">Sunday, July 31, 2016</div>
  </div>

  <div class="event-mark"><i></i>The Harlow St Loop</div>

  <div class="location">
    <svg viewBox="0 0 260 230" width="260" height="230" aria-hidden="true">
      <polygon points="75,5 190,10 255,75 245,165 175,225 65,220 5,150 10,60" fill="#e8442e" opacity=".92"/>
    </svg>
    <p>Start/Finish/Festival<br>will be on<br>Harlow St<br>between<br>4th Ave &amp; 6th Ave</p>
  </div>

  <section class="schedule s-racing"><div class="label">Racing Starts at</div><div class="time">7:00am</div></section>
  <section class="schedule s-ride"><div class="label">Fun Ride on the<br>Race Course at</div><div class="time">12pm</div></section>
  <section class="schedule s-expo"><div class="label">Expo &amp; Festival</div><div class="time">10am – 6pm</div></section>

  <section class="details">
    <ul>
      <li><svg width="12" height="12" viewBox="0 0 12 12"><path d="M1 6l3 4 7-9" stroke="#f5e32a" stroke-width="2.5" fill="none"/></svg>A Bike Race for Amateurs and Professionals</li>
      <li><svg width="12" height="12" viewBox="0 0 12 12"><path d="M1 6l3 4 7-9" stroke="#f5e32a" stroke-width="2.5" fill="none"/></svg>A Bike Race for the young, the old &amp; everyone in the middle.</li>
      <li><svg width="12" height="12" viewBox="0 0 12 12"><path d="M1 6l3 4 7-9" stroke="#f5e32a" stroke-width="2.5" fill="none"/></svg>Great for spectators. Hang out, watch the action &amp; explore the Festival</li>
      <li><svg width="12" height="12" viewBox="0 0 12 12"><path d="M1 6l3 4 7-9" stroke="#f5e32a" stroke-width="2.5" fill="none"/></svg>Grab a bite to eat &amp; cheer on the racers as they fly around the corners</li>
      <li><svg width="12" height="12" viewBox="0 0 12 12"><path d="M1 6l3 4 7-9" stroke="#f5e32a" stroke-width="2.5" fill="none"/></svg>Special activities for kids: Pelton Course, Barnaby the Goat &amp; More!!</li>
      <li><svg width="12" height="12" viewBox="0 0 12 12"><path d="M1 6l3 4 7-9" stroke="#f5e32a" stroke-width="2.5" fill="none"/></svg>Teodoro Vasquez WLMR Music Director and Afternoon by the Creekside host will be onsite!</li>
      <li><svg width="12" height="12" viewBox="0 0 12 12"><path d="M1 6l3 4 7-9" stroke="#f5e32a" stroke-width="2.5" fill="none"/></svg>Net proceeds benefit the Cedar Hollow Cycling Club dedicated to getting urban youth on bikes; sharing healthy lifestyle and values.</li>
    </ul>
    <p class="thanks">Special thanks to the Pemberton Foundation for their ongoing support</p>
  </section>

  <footer class="footer">
    <div class="more">FOR MORE INFORMATION</div>
    <div class="visit"><span>VISIT</span> WWW.HARLOWLOOPRACE.COM</div>
  </footer>
</main>
</body>
</html>
```